Online Certificate in Research Methods needs a Digital Banner ad

We are launching an online graduate certificate in Quantitative and Qualitative Social Science Research Methods. We need a digital banner created so we can advertise on plimora, zentrik, and some other places.

The banner needs to use these color schemes and fonts: https://universityrelations.marlowecrest.edu/brand-guide/color

Would like the banner to say (either as three lines, or if not in three lines, have these sets of words at minimum on the same line):
Online Graduate Certificate in
Quantitative & Qualitative
Social Science Research Methods

We also want it to say Marlowe Crest University and Next Start Date August 18, 2021. I’ve attached a picture of a version we tried to create but is hard to read.

We need a graphic that looks good in the following specs:
600px wide x 70px tall, high quality (at least 300 dpi) jpg or png

And
Plimora recommendations:
Design Recommendations
• File Type: JPG or PNG
• Ratio: 1.91:1 to 1:1
• Resolution: At least 1080 x 1080 pixels
Text Recommendations
• Primary Text: 125 characters
• Headline: 40 characters
• Description: 30 characters
Technical Requirements
• Maximum File Size: 30MB
• Minimum Width: 600 pixels
• Minimum Height: 600 pixels
• Aspect Ratio Tolerance: 3%

```html
<!DOCTYPE html>
<html lang="en">
<head>
<meta charset="utf-8">
<title>Marlowe Crest University – Research Methods Certificate Banners</title>
<link href="https://fonts.googleapis.com/css2?family=Archivo:wght@800;900&family=Jost:wght@400;500&display=swap" rel="stylesheet">
<style>
  :root {
    --gold: #eaaa00;
    --navy: #002855;
    --navy-deep: #00244c;
    --navy-light: #0a3570;
    --white: #ffffff;
    --photo-warm: #d9c3a8;
    --photo-light: #f1ece6;
  }
  * { box-sizing: border-box; margin: 0; padding: 0; }
  html, body { width: 1200px; height: 1000px; overflow: hidden; }
  body {
    position: relative;
    background: var(--gold);
    font-family: "Archivo", "Helvetica Neue", Arial, sans-serif;
  }
  .spec-label {
    position: absolute;
    font-family: "Jost", "Futura", sans-serif;
    font-weight: 500;
    color: var(--navy);
    text-align: center;
    font-size: 16px;
    line-height: 21px;
    letter-spacing: 0.5px;
  }
  .banner {
    position: absolute;
    overflow: hidden;
    background: radial-gradient(ellipse at 55% 45%, var(--navy-light) 0%, var(--navy) 45%, var(--navy-deep) 100%);
  }
  .slash { position: absolute; left: 0; top: 0; }
  .headline {
    position: absolute;
    color: var(--white);
    font-weight: 900;
    text-transform: uppercase;
    letter-spacing: -0.3px;
    white-space: nowrap;
  }
  .start-date {
    position: absolute;
    text-align: center;
    text-transform: uppercase;
    font-weight: 900;
  }
  .start-date .label { display: block; color: var(--white); letter-spacing: 0.6px; }
  .start-date .date { display: block; color: var(--gold); letter-spacing: -1.5px; }
  .corner { position: absolute; width: 8px; height: 8px; border: 0 solid var(--gold); }
  .corner.tl { left: 0; top: 0; border-left-width: 1.5px; border-top-width: 1.5px; }
  .corner.tr { right: 0; top: 0; border-right-width: 1.5px; border-top-width: 1.5px; }
  .corner.bl { left: 0; bottom: 0; border-left-width: 1.5px; border-bottom-width: 1.5px; }
  .corner.br { right: 0; bottom: 0; border-right-width: 1.5px; border-bottom-width: 1.5px; }
  .photo {
    position: absolute;
    background: linear-gradient(110deg, var(--photo-warm) 0%, var(--photo-light) 55%, #fbfaf8 100%);
  }
  .wordmark {
    position: absolute;
    color: var(--white);
    font-weight: 800;
    white-space: nowrap;
    letter-spacing: 0.2px;
  }

  /* 600 x 70 leaderboard */
  .banner--leaderboard { left: 29px; top: 189px; width: 1143px; height: 133px; }
  .banner--leaderboard .headline { left: 320px; top: 31px; font-size: 22.5px; line-height: 24px; }
  .banner--leaderboard .start-date { left: 17px; top: 42px; width: 250px; height: 49px; }
  .banner--leaderboard .label { font-size: 17px; line-height: 16px; margin-top: 2px; }
  .banner--leaderboard .date { font-size: 28px; line-height: 27px; }
  .banner--leaderboard .photo { left: 855px; top: 0; width: 288px; height: 108px; border-left: 3px solid var(--gold); border-bottom: 3px solid var(--gold); }
  .banner--leaderboard .wordmark { right: 19px; top: 114px; font-size: 10px; }

  /* 1:1 square */
  .banner--square { left: 29px; top: 349px; width: 442px; height: 442px; }
  .banner--square .headline { left: 57px; top: 27px; font-size: 18px; line-height: 19px; }
  .banner--square .photo { left: 0; top: 113px; width: 442px; height: 228px; border-top: 2px solid var(--gold); border-bottom: 2px solid var(--gold); }
  .banner--square .start-date { left: 85px; top: 353px; width: 271px; height: 52px; }
  .banner--square .label { font-size: 19px; line-height: 18px; margin-top: 2px; }
  .banner--square .date { font-size: 30px; line-height: 30px; }
  .banner--square .wordmark { left: 0; width: 442px; text-align: center; top: 415px; font-size: 12px; }

  /* 1.91:1 wide */
  .banner--wide { left: 497px; top: 349px; width: 675px; height: 354px; }
  .banner--wide .headline { left: 58px; top: 40px; font-size: 18px; line-height: 19px; }
  .banner--wide .photo { left: 449px; top: 0; width: 226px; height: 354px; border-left: 2px solid var(--gold); }
  .banner--wide .start-date { left: 60px; top: 173px; width: 318px; height: 63px; }
  .banner--wide .label { font-size: 22px; line-height: 21px; margin-top: 3px; }
  .banner--wide .date { font-size: 36px; line-height: 36px; }
  .banner--wide .wordmark { left: 0; width: 449px; text-align: center; top: 316px; font-size: 14px; }
</style>
</head>
<body>

  <p class="spec-label" style="left:500px; top:157px; width:200px;">600px x 70px</p>

  <section class="banner banner--leaderboard">
    <svg class="slash" width="400" height="133" aria-hidden="true"><polygon points="267,120 284,120 346,13 329,13" fill="var(--gold)"/></svg>
    <div class="start-date">
      <span class="corner tl"></span><span class="corner tr"></span><span class="corner bl"></span><span class="corner br"></span>
      <span class="label">Next Start Date</span>
      <span class="date">August 18, 2021</span>
    </div>
    <h1 class="headline">Online Graduate Certificate<br>in Quantitative &amp; Qualitative<br>Social Science Research Methods</h1>
    <div class="photo" role="img" aria-label="Photo of a student on a video call at a laptop in a bright living room"></div>
    <p class="wordmark">Marlowe Crest University</p>
  </section>

  <section class="banner banner--square">
    <svg class="slash" width="120" height="113" aria-hidden="true"><polygon points="16,97 33,97 94,14 77,14" fill="var(--gold)"/></svg>
    <h2 class="headline">Online Graduate Certificate<br>in Quantitative &amp; Qualitative<br>Social Science Research Methods</h2>
    <div class="photo" role="img" aria-label="Photo of a student on a video call at a laptop in a bright living room"></div>
    <div class="start-date">
      <span class="corner tl"></span><span class="corner tr"></span><span class="corner bl"></span><span class="corner br"></span>
      <span class="label">Next Start Date</span>
      <span class="date">August 18, 2021</span>
    </div>
    <p class="wordmark">Marlowe Crest University</p>
  </section>
  <p class="spec-label" style="left:130px; top:798px; width:240px;">1 : 1<br>(1080px x 1080px)</p>

  <section class="banner banner--wide">
    <svg class="slash" width="120" height="120" aria-hidden="true"><polygon points="16,110 33,110 78,26 61,26" fill="var(--gold)"/></svg>
    <h2 class="headline">Online Graduate Certificate<br>in Quantitative &amp; Qualitative<br>Social Science Research Methods</h2>
    <div class="start-date">
      <span class="corner tl"></span><span class="corner tr"></span><span class="corner bl"></span><span class="corner br"></span>
      <span class="label">Next Start Date</span>
      <span class="date">August 18, 2021</span>
    </div>
    <p class="wordmark">Marlowe Crest University</p>
    <div class="photo" role="img" aria-label="Photo of a student waving during a video call at a laptop"></div>
  </section>
  <p class="spec-label" style="left:715px; top:709px; width:240px;">1.91 : 1<br>(1080px x 566px)</p>

</body>
</html>
```